Lumen Heat Flow Studio – Corporate Brand Identity

We are in need of a full company image and brand identity design for a brand new hot yoga studio in a small but busy and wealthy oil town.
Our logo was designed through artbazaar and we currently have an open wordpress project in artbazaar with a deadline of July 14. We plan on continuing to build our marketing presence through artbazaar or one on one with designers that have been able to capture our vision easily. So, there are many more opportunities for continued projects.
We love our current logo and would like it to be utilized well. We want our logo to be familiar, known and synonymous with hot yoga in Alberta, Canada. We have intentions of opening up more locations and are looking for a strong brand that we can eventually franchise.
We need to display a strong but serene image that demands awe and communicates to people that Lumen Heat Flow is the real deal and will provide them with exactly what they need. Our studio is the perfect balance of what you would gain from going to a gym and developing your physical fitness and visiting a spa and nurturing a quiet mind, calm spirit and finding relaxation. We are all of this in one place. Breathe. Bend. Beam. – Steady Frame. Still Heart. Clear Soul.
In every detail our brand image should feel that “we are it.. the real deal when it comes to yoga…the place you want to be… the community you want to be apart of”. We need to appeal to men and women and a very important part of our business will be offering corporate packages and workplace yoga to the large oil companies in town. Our clientele is affluent so although we want creativity it still needs to be posh and upscale.
Most importantly, we are looking for something that is extraordinarily creative and show stopping. We want to set ourselves apart from all other studios in Canada, in terms of our creative, beautiful print marketing. When I say innovative, I’m thinking outside the box as in we want to be known for having beautiful and creative brand image http://www.quirkyfennel.com/fitness-and-yoga-ads/ I also like the idea of utilizing an image of the most beautiful oasis – see http://markgallerio.com/tulsi-flow-studio/
We are in need of at least the following:
- Business Cards – Front & Back
- Standard Letterhead (Size A4)
- Continuation Letterhead
- Envelopes (Sizes C4 & A4, , C5, DL)
- Postcard (for voucher, birthday, marketing)
- Loyalty Card design (front and back) for 10 visits
- Gift Certificate design
- Presentation Folder (for corporate packages)
- Standard Invoice A4 (word template)
- With Compliments Slips A5 (word template)
- Email Signature
OPTIONAL
- Labels for Branded Retail Products (Mat Spray, Room Spray, Aromatherapy)
- Social Media (Facebook Cover, etc)
All items must be editable in regards to changing names, addresses, etc. and high resolution please.
Please let me know if you require the logo in another format - ie. "ai, eps"

```html
<!DOCTYPE html>
<html lang="en">
<head>
<meta charset="utf-8">
<title>Lumen Heat Flow Studio – Letterhead</title>
<link rel="stylesheet" href="https://fonts.googleapis.com/css2?family=Tinos:ital,wght@0,400;0,700;1,400&family=Montserrat:wght@300;400&display=swap">
<style>
  :root {
    --backdrop: #e6e7e8;
    --paper: #ffffff;
    --ink: #1c1c1c;
    --teal: #2f9d94;
    --teal-light: #5ec4d0;
    --muted: #7b8385;
  }
  * { box-sizing: border-box; margin: 0; padding: 0; }
  html, body { width: 1200px; height: 909px; overflow: hidden; background: var(--backdrop); }
  .letterhead {
    position: absolute; left: 296px; top: 24px; width: 608px; height: 861px;
    background: var(--paper); box-shadow: 0 4px 18px rgba(0,0,0,.12); overflow: hidden;
    font-family: "Tinos", "Times New Roman", serif; color: var(--ink);
  }
  .brand-mark { position: absolute; left: 52px; top: 64px; display: flex; align-items: center; gap: 8px; }
  .brand-dot { width: 14px; height: 14px; border-radius: 50%; background: var(--teal); }
  .brand-name { font-family: "Tinos", serif; font-size: 15px; color: var(--teal); letter-spacing: .5px; }
  .contact-list {
    position: absolute; left: 372px; top: 58px; list-style: none;
    font-family: "Montserrat", sans-serif; font-weight: 300; font-size: 8px; color: var(--muted); line-height: 13px;
  }
  .contact-list li { display: flex; align-items: center; gap: 6px; }
  .contact-list .address { margin-bottom: 4px; }
  .contact-icon { width: 7px; height: 7px; border-radius: 50%; background: var(--teal); flex: none; }
  .letter-body { position: absolute; left: 52px; top: 170px; width: 470px; font-size: 11px; line-height: 14.5px; z-index: 1; }
  .salutation { font-weight: 700; margin-bottom: 12px; }
  .letter-body p { text-align: justify; margin-bottom: 12px; }
  .closing { margin-top: 44px; line-height: 14px; }
  .signature { display: block; width: 90px; height: 30px; margin: 6px 0 4px; background: linear-gradient(90deg, #d9d9d9, #efefef); border-radius: 3px; }
  .wave-area {
    position: absolute; left: 120px; top: 580px; width: 488px; height: 281px;
    background: linear-gradient(155deg, rgba(94,196,208,0) 45%, rgba(94,196,208,.55) 72%, var(--teal) 100%);
  }
</style>
</head>
<body>
<main class="letterhead">
  <div class="wave-area" role="img" aria-label="Teal sweeping wave ornament in the lower corner"></div>

  <div class="brand-mark">
    <span class="brand-dot"></span>
    <span class="brand-name">Lumen Heat Flow Studio</span>
  </div>

  <ul class="contact-list">
    <li class="address">Kestrel Lane 14, 4410 Marrow Bay</li>
    <li><span class="contact-icon"></span>+12 34 555 01 27</li>
    <li><span class="contact-icon"></span>+12 34 555 09 64</li>
    <li><span class="contact-icon"></span>r.halden@lumenheat.ex</li>
    <li><span class="contact-icon"></span>www.lumenheat.ex</li>
  </ul>

  <section class="letter-body">
    <p class="salutation">Gentlemen,</p>
    <p>Enclosed I have the honor to send you an article which I should be pleased if you would accept for the “Meridian Review.” I am <em>desperately</em> pushed for money; and in the event of Mr. Harrowgate’s liking the “Landscape-Garden” I would take it as an especial favor if you would mail me the amount due for it, so as to reach me here by the 21st, on which day I shall need it. Can you possibly oblige me in this? If you accept the paper I presume you will allow me your usual sum, whatever that is for similar contributions—but I set no price—leaving all to your own liberality. The piece will make 8 of your pages and rather more.</p>
    <p>Will you be kind enough to put the best possible interpretation upon my behavior while in Port Ardent? You must have conceived a <em>queer</em> idea of me—but the simple truth is that Lindqvist would insist upon <em>the juleps</em>, and I knew not what I was either doing or saying. The Review of Corbel which I offered you was deficient in a 1/2 page of commencement, which I had written to supersede the old beginning, and which gave the article the character of a general and retrospective review. No wonder you did not take it—I would have been very much mortified if you had. I hope to see you at some future time, under better auspices.</p>
    <div class="closing">
      In the meantime I remain<br>
      Yours very truly,
      <span class="signature" role="img" aria-label="Handwritten signature of the sender"></span>
      Everett Alden Pryce
    </div>
  </section>
</main>
</body>
</html>
```